Business Cards for a start up company

We are looking for a business card design for a start up company based in Ohio. The logo is attached. We are a healthcare company. We are open to all designs but want something professional but fun; creative, not boring

Industry/Entity Type

Healthcare

```html
<!DOCTYPE html>
<html lang="en">
<head>
<meta charset="utf-8">
<title>Bright Link Care – Business Cards</title>
<link rel="stylesheet" href="https://fonts.googleapis.com/css2?family=Playfair+Display:wght@400&family=Arimo:wght@400&display=swap">
<style>
  :root {
    --stage: #2e2c38;
    --card-white: #ffffff;
    --cyan: #2ac3ea;
    --cyan-light: #46d0f3;
    --cyan-faint: rgba(255, 255, 255, 0.18);
    --navy: #1f2a5c;
    --green: #8cc63f;
    --text-white: #ffffff;
  }
  * { box-sizing: border-box; margin: 0; padding: 0; }
  html, body {
    width: 1200px;
    height: 800px;
    overflow: hidden;
    background: var(--stage);
  }
  .stage {
    position: relative;
    width: 1200px;
    height: 800px;
  }
  .card {
    position: absolute;
    width: 520px;
    height: 297px;
    background: var(--card-white);
    overflow: hidden;
    box-shadow: 0 12px 30px rgba(0, 0, 0, 0.35);
  }
  .card--contact { left: 50px; top: 252px; }
  .card--identity { left: 630px; top: 252px; }
  .card__shapes {
    position: absolute;
    inset: 0;
    width: 100%;
    height: 100%;
  }
  .brand {
    position: absolute;
    left: 92px;
    top: 100px;
    display: flex;
    align-items: center;
    gap: 12px;
  }
  .brand__dot {
    width: 40px;
    height: 40px;
    border-radius: 50%;
    background: var(--green);
  }
  .brand__name {
    font-family: "Playfair Display", Georgia, serif;
    font-weight: 400;
    font-size: 29px;
    color: var(--navy);
    letter-spacing: 0.2px;
  }
  .details {
    position: absolute;
    top: 166px;
    left: 0;
    width: 100%;
    font-family: "Arimo", Arial, sans-serif;
    font-size: 14px;
    line-height: 17px;
  }
  .details__row {
    display: flex;
  }
  .details__label {
    width: 208px;
    text-align: right;
    padding-right: 6px;
    color: var(--navy);
  }
  .card--identity .details__label { color: var(--green); }
  .details__value {
    color: var(--text-white);
  }
  .details__value--caps { text-transform: uppercase; }
</style>
</head>
<body>
<main class="stage">

  <section class="card card--contact" aria-label="Business card, contact side">
    <svg class="card__shapes" viewBox="0 0 520 297" aria-hidden="true">
      <polygon points="0,0 120,0 120,62 0,78" fill="var(--cyan)"/>
      <polygon points="190,0 520,0 520,92 190,66" fill="var(--cyan)"/>
      <polygon points="0,196 120,206 120,297 0,297" fill="var(--cyan)"/>
      <polygon points="208,166 520,150 520,297 208,297" fill="var(--cyan-light)"/>
      <circle cx="420" cy="238" r="62" fill="none" stroke="var(--cyan-faint)" stroke-width="16"/>
    </svg>
    <div class="brand">
      <span class="brand__dot"></span>
      <span class="brand__name">Bright Link Care</span>
    </div>
    <div class="details">
      <div class="details__row"><span class="details__label">phone:</span><span class="details__value">555-014-2276</span></div>
      <div class="details__row"><span class="details__label">email:</span><span class="details__value">brightlinkcare@com</span></div>
      <div class="details__row"><span class="details__label">Address:</span><span class="details__value">#000, Bright Link Care</span></div>
      <div class="details__row"><span class="details__label"></span><span class="details__value">Riverton, TX 75001</span></div>
    </div>
  </section>

  <section class="card card--identity" aria-label="Business card, name side">
    <svg class="card__shapes" viewBox="0 0 520 297" aria-hidden="true">
      <polygon points="0,0 120,0 120,62 0,78" fill="var(--cyan)"/>
      <polygon points="190,0 520,0 520,92 190,66" fill="var(--cyan)"/>
      <polygon points="0,196 120,206 120,297 0,297" fill="var(--cyan)"/>
      <polygon points="208,166 520,150 520,297 208,297" fill="var(--cyan-light)"/>
      <circle cx="420" cy="238" r="62" fill="none" stroke="var(--cyan-faint)" stroke-width="16"/>
    </svg>
    <div class="brand">
      <span class="brand__dot"></span>
      <span class="brand__name">Bright Link Care</span>
    </div>
    <div class="details">
      <div class="details__row"><span class="details__label">name:</span><span class="details__value details__value--caps">Bright Link Care</span></div>
      <div class="details__row"><span class="details__label">designation:</span><span class="details__value details__value--caps">CEO/President</span></div>
    </div>
  </section>

</main>
</body>
</html>
```